Willowmere Elder Guides (WEG) business card and logo

I need a business card and logo that stands out of the crowd!!! This business is a health care placement agency. I need it to show confidence and compassion BUT be very modern please. I want the back with the information side to look like the black card and the color palette inspiration is the blue and rose gold the top photo is the logo inspiration idea! But I’m open to other things.
Updates

I have a picture of the color design that I want my business card to have- Designers, would you also mock up the color with the business card. I would like to see that blue hue and rose gold variation so that I can get a really good picture.

Industry/Entity Type

Healthcare placement agency- client based business, meeting and touring businesses with clients.

Contact Information for Business Card

I’ve given a photo inspiration for the back of the card, the how to reach me section. I’m wanting to have a QR code placed, room for email, phone, website.

Font styles to use
Script
Other font styles liked:
• Open to many design options- I do want clean but a bit soft and relatable

Requirements
Must have
• Brand expansion ability, either an acronym as the logo, the E possibly, or the design needs to have a sleek, confident modern feel.
Nice to have
• QR code, ability to have raised texture in the background of the card for an extra flair and look, but not too in your face.

```html
<!DOCTYPE html>
<html lang="en">
<head>
<meta charset="utf-8">
<title>Willowmere Elder Guides – Business Card</title>
<link rel="stylesheet" href="https://fonts.googleapis.com/css2?family=Cinzel:wght@400&family=Montserrat:wght@400;700&display=swap">
<style>
  :root {
    --backdrop: #1c1b1d;
    --card: #121113;
    --rose: #e2a097;
    --rose-soft: #c9877f;
    --rose-edge: #f0b2a8;
  }
  * { margin: 0; padding: 0; box-sizing: border-box; }
  html, body { width: 1200px; height: 900px; overflow: hidden; background: var(--backdrop); }
  .canvas { position: relative; width: 1200px; height: 900px; }

  .card {
    position: absolute;
    width: 600px; height: 343px;
    background: var(--card);
    border-radius: 18px;
    box-shadow: 0 3px 0 var(--rose-edge), 0 18px 40px rgba(0,0,0,.55);
    color: var(--rose);
  }
  .card--info { left: 90px; top: 80px; }
  .card--brand { left: 510px; top: 477px; }

  .brand-lockup {
    position: absolute;
    display: flex; flex-direction: column; align-items: center;
    font-family: "Cinzel", serif; font-weight: 400; color: var(--rose);
    text-align: center; line-height: 1.12; letter-spacing: .04em;
  }
  .brand-mark { border: 2px solid var(--rose); border-radius: 50%; }
  .card--info .brand-lockup { left: 40px; top: 62px; width: 300px; }
  .card--info .brand-mark { width: 92px; height: 92px; margin-bottom: 18px; }
  .card--info .brand-name { font-size: 26px; }
  .card--brand .brand-lockup { left: 120px; top: 52px; width: 360px; }
  .card--brand .brand-mark { width: 110px; height: 110px; margin-bottom: 22px; }
  .card--brand .brand-name { font-size: 32px; }

  .divider {
    position: absolute; left: 362px; top: 70px;
    width: 1px; height: 205px; background: var(--rose-soft);
  }

  .contact {
    position: absolute; left: 388px; top: 68px; width: 200px;
    font-family: "Montserrat", sans-serif; color: var(--rose);
  }
  .contact-name { font-weight: 700; font-size: 18px; }
  .contact-role { font-size: 11px; margin-bottom: 16px; }
  .contact-address { font-size: 11px; line-height: 1.45; margin-bottom: 14px; }
  .contact-list { list-style: none; font-size: 11px; }
  .contact-list li { display: flex; align-items: center; gap: 8px; height: 20px; }
  .contact-list svg { width: 11px; height: 11px; flex: none; fill: var(--rose); }
</style>
</head>
<body>
<main class="canvas">

  <section class="card card--info">
    <div class="brand-lockup">
      <div class="brand-mark"></div>
      <div class="brand-name">Willowmere<br>Elder Guides</div>
    </div>
    <div class="divider"></div>
    <div class="contact">
      <div class="contact-name">Corin Ashdale</div>
      <div class="contact-role">Owner</div>
      <div class="contact-address">418 Larkspur Ave, #12<br>Fairhaven, OH 43190</div>
      <ul class="contact-list">
        <li><svg viewBox="0 0 12 12"><path d="M1 4c0-2 2-3 5-3s5 1 5 3l-2 1-1-1.5H4L3 5zM2.5 6h7l1 5h-9z"/></svg>800-555-0142</li>
        <li><svg viewBox="0 0 12 12"><path d="M3 0h6v12H3zM4 1.5v8h4v-8z"/></svg>800-555-0143</li>
        <li><svg viewBox="0 0 12 12"><path d="M3 0h5v3H3zM1 4h10v6H1zM3 10h6v2H3z"/></svg>800-555-0144</li>
        <li><svg viewBox="0 0 12 12"><path d="M0 2h12v8H0zM1 3l5 4 5-4z" fill-rule="evenodd"/></svg>hello@willowmereguides.com</li>
        <li><svg viewBox="0 0 12 12"><path d="M6 0a6 6 0 1 0 0 12A6 6 0 0 0 6 0zm0 1.5c1 1 1.5 2.8 1.5 4.5S7 9.5 6 10.5C5 9.5 4.5 7.7 4.5 6S5 2.5 6 1.5z" fill-rule="evenodd"/></svg>www.willowmereguides.com</li>
      </ul>
    </div>
  </section>

  <section class="card card--brand">
    <div class="brand-lockup">
      <div class="brand-mark"></div>
      <div class="brand-name">Willowmere<br>Elder Guides</div>
    </div>
  </section>

</main>
</body>
</html>
```